Process Roadmap for Interior Design Firm

We are looking to ramp up the design appeal of our current process roadmap to be very visually interesting, while staying informative and descriptive about our process.

Target Market(s)

In-house Clients

Industry/Entity Type

Interior Design Firm focused on sustainable and holistic design.

Other font styles liked:
• raleway

Requirements
Must have
• 1.) it would be nice if the graphic provided a more clear indication of the “journey” from one step to the next, so that there was a clear sense of the progression (such that we are directing the viewer) 2.). We would want it to fit on an 8.5”x11” page (the page could be horizontal when we have the Steady Pathway formatted out with the testimonials) (in addition to the testimonials, we may also want to have the detailed descriptions of each step of the process presented below the graphic, so that the graphic is cleaner) 3.) ideally the graphic is clear and simple enough to also be used on our Bi-Weekly Client Updates, which will be typed updates for clients re their project budgets, schedule and scope. The Steady Pathway graphic (without all the testimonials) would be at the end of the update, and would fit on the page horizontally at the bottom, perhaps in a space which is 7.5”w x 4”h or so.
Should not have
• bold or bright colors. Natural neutrals are preferred, such as the ones featured on the provided graphic.

```html
<!DOCTYPE html>
<html lang="en">
<head>
<meta charset="utf-8">
<title>HRD Steady Pathway</title>
<link href="https://fonts.googleapis.com/css2?family=Raleway:wght@300;400;500;600&family=Montserrat:wght@500;700&display=swap" rel="stylesheet">
<style>
  :root {
    --gold: #b8914a;
    --gold-soft: #c8aa70;
    --gold-pale: #d9c79f;
    --band: #ebe4d2;
    --line: #e6dcc6;
    --text: #b4975f;
    --paper: #ffffff;
    --avatar: #f1e8d4;
    --shadow: rgba(150, 125, 80, 0.18);
  }
  * { box-sizing: border-box; margin: 0; padding: 0; }
  html, body { width: 1200px; height: 2337px; overflow: hidden; background: var(--paper); }
  body { position: relative; font-family: 'Raleway', sans-serif; color: var(--text); }

  .format-title { position: absolute; left: 0; width: 1186px; text-align: center; line-height: 1.1; }
  .format-title .size { display: block; font-size: 33px; font-weight: 300; color: var(--gold-soft); }
  .format-title .kind { display: block; font-size: 40px; font-weight: 600; color: var(--gold); }

  .infographic-frame { position: absolute; border: 1.5px solid var(--line); border-radius: 20px; background: var(--paper); }
  .infographic-frame svg { display: block; width: 100%; height: 100%; }
  .frame-large { left: 69px; top: 204px; width: 1034px; height: 552px; }
  .frame-small { left: 142px; top: 1193px; width: 872px; height: 463px; border-radius: 16px; }

  .page-sheet { position: absolute; left: 79px; top: 938px; width: 1016px; height: 1314px; border: 1.5px solid var(--line); }

  .brand { position: absolute; left: 459px; top: 1024px; display: flex; align-items: center; gap: 22px; }
  .brand-square { width: 30px; height: 30px; border: 2px solid var(--gold-soft); }
  .brand-name { font-family: 'Raleway', sans-serif; font-weight: 400; font-size: 26px; letter-spacing: 7px; color: var(--gold); line-height: 1.25; }

  .testimonials-title { position: absolute; left: 79px; width: 1016px; top: 1708px; text-align: center; font-size: 36px; font-weight: 300; color: var(--gold-soft); }

  .testimonial { position: absolute; width: 403px; height: 118px; background: var(--paper); border-radius: 16px; box-shadow: 0 3px 6px var(--shadow); border: 1px solid var(--line); }
  .testimonial .tail { position: absolute; right: -34px; top: -1px; width: 40px; height: 50px; overflow: visible; }
  .testimonial .avatar { position: absolute; left: 38px; top: 25px; width: 68px; height: 68px; border-radius: 50%; background: var(--avatar); }
  .testimonial .stars { position: absolute; left: 145px; top: 24px; display: flex; gap: 13px; }
  .testimonial .stars svg { width: 28px; height: 27px; }
  .testimonial .quote { position: absolute; left: 130px; width: 240px; top: 64px; font-size: 8.6px; line-height: 1.2; text-align: center; color: var(--text); }

  .col-left { left: 142px; }
  .col-right { left: 607px; }
  .row-1 { top: 1796px; }
  .row-2 { top: 1942px; }
  .row-3 { top: 2087px; }

  /* roadmap graphic */
  .rm-title { font-family: 'Montserrat', sans-serif; font-weight: 700; font-size: 28px; fill: var(--gold); }
  .rm-subtitle { font-family: 'Raleway', sans-serif; font-weight: 300; font-size: 29px; fill: var(--gold); }
  .rm-seven { font-family: 'Montserrat', sans-serif; font-weight: 700; font-size: 22px; fill: var(--gold); }
  .rm-step { font-family: 'Montserrat', sans-serif; font-weight: 500; font-size: 10px; fill: var(--gold); }
  .rm-num { font-family: 'Montserrat', sans-serif; font-weight: 700; font-size: 14px; fill: var(--gold); }
  .rm-label { font-family: 'Raleway', sans-serif; font-weight: 400; font-size: 16.5px; fill: var(--gold); }
  .rm-desc { font-family: 'Raleway', sans-serif; font-weight: 400; font-size: 7.6px; fill: var(--text); text-anchor: middle; }
  .rm-icon { fill: none; stroke: var(--gold); stroke-width: 1.2; stroke-linecap: round; stroke-linejoin: round; }
</style>
</head>
<body>

<svg width="0" height="0" style="position:absolute" aria-hidden="true">
  <defs>
    <g id="step-badge">
      <circle r="38" fill="#fff" stroke="var(--line)" stroke-width="1.2"/>
      <path d="M-29 0 A29 29 0 0 1 29 0" fill="none" stroke="var(--gold)" stroke-width="7"/>
      <circle r="23" fill="#fff" stroke="var(--gold-pale)" stroke-width="0.9"/>
      <polyline points="-7,42 0,48 7,42" fill="none" stroke="var(--gold-pale)" stroke-width="1"/>
    </g>
    <symbol id="roadmap" viewBox="0 0 750 400">
      <!-- dotted arc -->
      <g fill="var(--gold-pale)">
        <circle cx="108" cy="47" r="2.2"/><circle cx="163" cy="70" r="2.2"/><circle cx="193" cy="94" r="2.2"/>
        <circle cx="262" cy="124" r="2.2"/><circle cx="335" cy="142" r="2.2"/><circle cx="375" cy="144" r="2.2"/>
        <circle cx="418" cy="142" r="2.2"/><circle cx="490" cy="124" r="2.2"/><circle cx="553" cy="94" r="2.2"/>
        <circle cx="583" cy="70" r="2.2"/><circle cx="610" cy="48" r="2.2"/>
      </g>

      <!-- title -->
      <text class="rm-title" x="373" y="47" text-anchor="middle">HRD</text>
      <circle cx="260" cy="74" r="16" fill="none" stroke="var(--gold-pale)" stroke-width="2"/>
      <text class="rm-seven" x="260" y="82" text-anchor="middle">7</text>
      <text class="rm-subtitle" x="290" y="84">Steady Pathway</text>

      <!-- journey band -->
      <path d="M72 97 C100 140 120 160 156 167 S220 190 256 197 S330 220 363 220 S430 205 470 197 S540 180 576 167 S640 140 669 97"
            fill="none" stroke="var(--band)" stroke-width="20" stroke-linecap="round"/>

      <!-- step badges -->
      <use href="#step-badge" x="72" y="97"/>
      <use href="#step-badge" x="156" y="167"/>
      <use href="#step-badge" x="256" y="197"/>
      <use href="#step-badge" x="363" y="220"/>
      <use href="#step-badge" x="470" y="197"/>
      <use href="#step-badge" x="576" y="167"/>
      <use href="#step-badge" x="669" y="97"/>

      <!-- step numbers -->
      <g text-anchor="middle">
        <text class="rm-step" x="72" y="46">STEP</text><text class="rm-num" x="72" y="60">01</text>
        <text class="rm-step" x="156" y="116">STEP</text><text class="rm-num" x="156" y="130">02</text>
        <text class="rm-step" x="256" y="146">STEP</text><text class="rm-num" x="256" y="160">03</text>
        <text class="rm-step" x="363" y="175">STEP</text><text class="rm-num" x="363" y="189">04</text>
        <text class="rm-step" x="470" y="148">STEP</text><text class="rm-num" x="470" y="162">05</text>
        <text class="rm-step" x="576" y="116">STEP</text><text class="rm-num" x="576" y="130">06</text>
        <text class="rm-step" x="669" y="46">STEP</text><text class="rm-num" x="669" y="60">07</text>
      </g>

      <!-- icons -->
      <g class="rm-icon">
        <g transform="translate(72 97)">
          <rect x="-9" y="-14" width="18" height="9" rx="2"/><circle cx="-7" cy="3" r="3"/><circle cx="7" cy="3" r="3"/>
          <path d="M-13 13 Q-7 6 -1 13 M1 13 Q7 6 13 13"/>
        </g>
        <g transform="translate(156 167)">
          <path d="M-13 -1 L0 -13 L13 -1"/><rect x="-10" y="-1" width="20" height="14"/><rect x="-6" y="4" width="6" height="6"/><path d="M3 4 h5 M3 7 h5 M3 10 h5"/>
        </g>
        <g transform="translate(256 197)">
          <rect x="-13" y="-11" width="26" height="18" rx="1"/><path d="M-13 -6 h26"/><circle cx="-6" cy="3" r="4"/><path d="M2 0 h7 M2 4 h7 M0 7 v6 M-4 13 h8"/>
        </g>
        <g transform="translate(363 220)">
          <circle cx="0" cy="-11" r="2.5"/><path d="M-1 -9 L-9 13 M1 -9 L9 13 M-6 5 h12"/><path d="M6 -14 A12 12 0 0 1 14 2"/>
        </g>
        <g transform="translate(470 197)">
          <rect x="-12" y="-12" width="20" height="18"/><path d="M-2 -12 v18 M-12 -3 h20"/><circle cx="3" cy="10" r="4"/><path d="M10 2 l3 3 -5 6"/>
        </g>
        <g transform="translate(576 167)">
          <circle cx="-6" cy="3" r="6"/><circle cx="6" cy="3" r="6"/><path d="M-9 -3 L-6 -11 H-2 V-3 M9 -3 L6 -11 H2 V-3"/>
        </g>
        <g transform="translate(669 97)">
          <path d="M-13 -1 L0 -13 L13 -1"/><rect x="-10" y="-1" width="20" height="14"/><circle cx="0" cy="5" r="4.5"/><path d="M9 -12 q5 -2 6 3 q-5 1 -6 -3"/>
        </g>
      </g>

      <!-- labels -->
      <g fill="var(--gold-pale)">
        <circle cx="35" cy="157" r="2"/><circle cx="118" cy="223" r="2"/><circle cx="218" cy="255" r="2"/>
        <circle cx="323" cy="285" r="2"/><circle cx="433" cy="255" r="2"/><circle cx="538" cy="224" r="2"/><circle cx="630" cy="157" r="2"/>
      </g>
      <text class="rm-label" x="42" y="163">Listening</text>
      <text class="rm-label" x="125" y="229">Visioning</text>
      <text class="rm-label" x="225" y="261">Planning</text>
      <text class="rm-label" x="330" y="291">Designing</text>
      <text class="rm-label" x="440" y="261">Managing</text>
      <text class="rm-label" x="545" y="230">Installing</text>
      <text class="rm-label" x="637" y="163">Completing</text>

      <!-- descriptions -->
      <text class="rm-desc" x="74" y="183">
        <tspan x="74">Listening to our</tspan><tspan x="74" dy="9">clients, their land,</tspan><tspan x="74" dy="9">and their home</tspan>
        <tspan x="74" dy="18">Identifying their</tspan><tspan x="74" dy="9">needs,challenges,</tspan><tspan x="74" dy="9">wishes, and</tspan><tspan x="74" dy="9">dreams.</tspan>
      </text>
      <text class="rm-desc" x="157" y="251">
        <tspan x="157">Facilitating a guided</tspan><tspan x="157" dy="9">visioning process to</tspan><tspan x="157" dy="9">clarify the deepest</tspan><tspan x="157" dy="9">intention, true purpose,</tspan><tspan x="157" dy="9">and highest potential</tspan><tspan x="157" dy="9">for their home and their</tspan><tspan x="157" dy="9">future within it.</tspan>
      </text>
      <text class="rm-desc" x="255" y="278">
        <tspan x="255">Turning our client's</tspan><tspan x="255" dy="9">vision into a clearly</tspan><tspan x="255" dy="9">defined scope, budget,</tspan><tspan x="255" dy="9">and timeline.</tspan>
        <tspan x="255" dy="15">Mapping out the steps</tspan><tspan x="255" dy="9">for making their dream</tspan><tspan x="255" dy="9">a reality.</tspan>
        <tspan x="255" dy="15">Setting a meeting</tspan><tspan x="255" dy="9">schedule from start</tspan><tspan x="255" dy="9">to finish.</tspan>
      </text>
      <text class="rm-desc" x="363" y="312">
        <tspan x="363">Following the schedule</tspan><tspan x="363" dy="9">through the design phases</tspan><tspan x="363" dy="9">from initial design concepts,</tspan><tspan x="363" dy="9">technical drawings and</tspan><tspan x="363" dy="9">details, and the selection of</tspan><tspan x="363" dy="9">all finishes, fixtures, and</tspan><tspan x="363" dy="9">furnishings.</tspan>
      </text>
      <text class="rm-desc" x="474" y="279">
        <tspan x="474">Coordinating with clients,</tspan><tspan x="474" dy="9">builders, architects, and</tspan><tspan x="474" dy="9">vendors to ensure that</tspan><tspan x="474" dy="9">the design is executed</tspan><tspan x="474" dy="9">with excellence,</tspan><tspan x="474" dy="9">and the construction and</tspan><tspan x="474" dy="9">furnishings are on-time</tspan><tspan x="474" dy="9">and on-budget.</tspan>
      </text>
      <text class="rm-desc" x="576" y="251">
        <tspan x="576">Overseeing the</tspan><tspan x="576" dy="9">inspection, installation,</tspan><tspan x="576" dy="9">and arrangement of all</tspan><tspan x="576" dy="9">furnishings, lighting,</tspan><tspan x="576" dy="9">artwork, and</tspan><tspan x="576" dy="9">decorative items.</tspan><tspan x="576" dy="9">Taking care of every</tspan><tspan x="576" dy="9">last detail.</tspan>
      </text>
      <text class="rm-desc" x="675" y="183">
        <tspan x="675">Fixing any issues</tspan><tspan x="675" dy="9">or defects.</tspan>
        <tspan x="675" dy="15">Follow up on all</tspan><tspan x="675" dy="9">remaining items</tspan>
        <tspan x="675" dy="15">Completing</tspan><tspan x="675" dy="9">the final finishing</tspan><tspan x="675" dy="9">touches to our</tspan><tspan x="675" dy="9">client's full and total</tspan><tspan x="675" dy="9">satisfaction.</tspan>
      </text>
    </symbol>
    <symbol id="star" viewBox="0 0 24 23">
      <polygon points="12,1 15,8.5 23,9 17,14.2 19,22 12,17.8 5,22 7,14.2 1,9 9,8.5" fill="#efe5cd" stroke="var(--gold-pale)" stroke-width="1"/>
    </symbol>
    <symbol id="bubble-tail" viewBox="0 0 40 50">
      <polygon points="0,0.5 18,0.5 38,26 0,48" fill="#fff" stroke="var(--line)" stroke-width="1"/>
      <rect x="0" y="1.5" width="2" height="46" fill="#fff"/>
    </symbol>
  </defs>
</svg>

<header class="format-title" style="top:68px">
  <span class="size">7.5”w x 4”h</span>
  <span class="kind">Infographic</span>
</header>

<section class="infographic-frame frame-large">
  <svg viewBox="0 0 750 400" role="img" aria-label="HRD 7 step Steady Pathway roadmap"><use href="#roadmap"/></svg>
</section>

<header class="format-title" style="top:808px">
  <span class="size">8.5”x11”</span>
  <span class="kind">Page</span>
</header>

<section class="page-sheet" aria-label="Letter page layout"></section>

<div class="brand">
  <span class="brand-square"></span>
  <span class="brand-name">HOLLIS REED<br>DESIGN</span>
</div>

<section class="infographic-frame frame-small">
  <svg viewBox="0 0 750 400" role="img" aria-label="HRD 7 step Steady Pathway roadmap"><use href="#roadmap"/></svg>
</section>

<h2 class="testimonials-title">Testimonials</h2>

<article class="testimonial col-left row-1">
  <svg class="tail"><use href="#bubble-tail"/></svg>
  <div class="avatar" role="img" aria-label="Client portrait"></div>
  <div class="stars"><svg><use href="#star"/></svg><svg><use href="#star"/></svg><svg><use href="#star"/></svg><svg><use href="#star"/></svg><svg><use href="#star"/></svg></div>
  <p class="quote">Lorem ipsum dolor sit amet, consectetuer adipiscing elit, sed diam nonummy nibh euismod tincidunt ut laoreet dolore magna aliquam erat volutpat.</p>
</article>
<article class="testimonial col-right row-1">
  <svg class="tail"><use href="#bubble-tail"/></svg>
  <div class="avatar" role="img" aria-label="Client portrait"></div>
  <div class="stars"><svg><use href="#star"/></svg><svg><use href="#star"/></svg><svg><use href="#star"/></svg><svg><use href="#star"/></svg><svg><use href="#star"/></svg></div>
  <p class="quote">Lorem ipsum dolor sit amet, consectetuer adipiscing elit, sed diam nonummy nibh euismod tincidunt ut laoreet dolore magna aliquam erat volutpat.</p>
</article>
<article class="testimonial col-left row-2">
  <svg class="tail"><use href="#bubble-tail"/></svg>
  <div class="avatar" role="img" aria-label="Client portrait"></div>
  <div class="stars"><svg><use href="#star"/></svg><svg><use href="#star"/></svg><svg><use href="#star"/></svg><svg><use href="#star"/></svg></div>
  <p class="quote">Lorem ipsum dolor sit amet, consectetuer adipiscing elit, sed diam nonummy nibh euismod tincidunt ut laoreet dolore magna aliquam erat volutpat.</p>
</article>
<article class="testimonial col-right row-2">
  <svg class="tail"><use href="#bubble-tail"/></svg>
  <div class="avatar" role="img" aria-label="Client portrait"></div>
  <div class="stars"><svg><use href="#star"/></svg><svg><use href="#star"/></svg><svg><use href="#star"/></svg><svg><use href="#star"/></svg><svg><use href="#star"/></svg></div>
  <p class="quote">Lorem ipsum dolor sit amet, consectetuer adipiscing elit, sed diam nonummy nibh euismod tincidunt ut laoreet dolore magna aliquam erat volutpat.</p>
</article>
<article class="testimonial col-left row-3">
  <svg class="tail"><use href="#bubble-tail"/></svg>
  <div class="avatar" role="img" aria-label="Client portrait"></div>
  <div class="stars"><svg><use href="#star"/></svg><svg><use href="#star"/></svg><svg><use href="#star"/></svg><svg><use href="#star"/></svg><svg><use href="#star"/></svg></div>
  <p class="quote">Lorem ipsum dolor sit amet, consectetuer adipiscing elit, sed diam nonummy nibh euismod tincidunt ut laoreet dolore magna aliquam erat volutpat.</p>
</article>
<article class="testimonial col-right row-3">
  <svg class="tail"><use href="#bubble-tail"/></svg>
  <div class="avatar" role="img" aria-label="Client portrait"></div>
  <div class="stars"><svg><use href="#star"/></svg><svg><use href="#star"/></svg><svg><use href="#star"/></svg><svg><use href="#star"/></svg><svg><use href="#star"/></svg></div>
  <p class="quote">Lorem ipsum dolor sit amet, consectetuer adipiscing elit, sed diam nonummy nibh euismod tincidunt ut laoreet dolore magna aliquam erat volutpat.</p>
</article>

</body>
</html>
```